Maplecrest Apartments Downtown Northport

We are looking to redesign our entry way sign at Maplecrest Apartments, a low density residential apartment building, located in Downtown Northport, Alabama, U.S. Downtown Northport is a bustling boutique business district with a small town feel comprised of shops, restaurants, and a renowned arts community known for Varrow Arts Center and Festival which is one of the nation's top outdoor arts festivals. Maplecrest Apartments and its sign is the first thing you seen when you enter Downtown Northport. We are looking to redesign our sign, entry way and landscaping to compliment the building and character of the historic downtown.

Target Market(s)

Our apartment building is comprised of 20 apartments units with tenants who are primarily part of the local workforce, young professionals, or students at the Halverton College or other nearby institutions.

Requirements
Must have
• The name of the apartment building - Maplecrest
Phone number on the sign 205-555-0148

```html
<!DOCTYPE html>
<html lang="en">
<head>
<meta charset="utf-8">
<title>Maplecrest Entry Sign</title>
<link rel="stylesheet" href="https://fonts.googleapis.com/css2?family=Stint+Ultra+Condensed&family=Michroma&display=swap">
<style>
  :root {
    --backdrop: #ecebe7;
    --sign-taupe: #8b7d67;
    --sign-white: #ffffff;
    --sky-blue: #6f9fd6;
    --siding-grey: #c9ced3;
    --lawn-green: #5f8f3a;
    --render-grey: #9a9a9a;
    --render-light: #e6e6e6;
  }
  * { box-sizing: border-box; margin: 0; padding: 0; }
  html, body {
    width: 1200px;
    height: 1038px;
    overflow: hidden;
    background: var(--backdrop);
  }
  .canvas {
    width: 1200px;
    height: 1038px;
    display: flex;
    align-items: center;
    justify-content: center;
  }
  .entry-sign {
    width: 1100px;
    height: 720px;
    background: var(--sign-taupe);
    display: flex;
    flex-direction: column;
    align-items: center;
    padding: 30px 60px 0;
    overflow: hidden;
    box-shadow: 0 6px 18px rgba(0,0,0,0.18);
  }
  .sign-name {
    font-family: "Stint Ultra Condensed", serif;
    font-weight: 400;
    color: var(--sign-white);
    font-size: 220px;
    line-height: 1;
    letter-spacing: 8px;
    white-space: nowrap;
    text-transform: uppercase;
    max-width: 980px;
    transform: scaleY(1.25);
    margin: 28px 0 36px;
  }
  .photo-row {
    display: flex;
    gap: 16px;
    width: 100%;
    justify-content: center;
  }
  .photo-frame {
    width: 318px;
    height: 198px;
    background: var(--sign-white);
    padding: 7px;
  }
  .photo-fill {
    width: 100%;
    height: 100%;
  }
  .photo-fill.building-exterior {
    background: linear-gradient(180deg, var(--sky-blue) 0%, var(--sky-blue) 30%, var(--siding-grey) 31%, var(--siding-grey) 72%, var(--lawn-green) 73%, var(--lawn-green) 100%);
  }
  .photo-fill.unit-floorplan {
    background: radial-gradient(ellipse at 50% 55%, var(--render-grey) 0%, #7a7a7a 35%, var(--render-light) 60%, #f4f4f4 100%);
  }
  .sign-phone {
    font-family: "Michroma", sans-serif;
    color: var(--sign-white);
    font-size: 66px;
    letter-spacing: 6px;
    white-space: nowrap;
    margin-top: 26px;
  }
</style>
</head>
<body>
  <main class="canvas">
    <section class="entry-sign">
      <h1 class="sign-name">Maplecrest</h1>
      <div class="photo-row">
        <div class="photo-frame">
          <div class="photo-fill building-exterior" role="img" aria-label="Photo of the Maplecrest apartment building exterior with lawn and white picket fence"></div>
        </div>
        <div class="photo-frame">
          <div class="photo-fill unit-floorplan" role="img" aria-label="3D rendered floor plan of an apartment unit"></div>
        </div>
        <div class="photo-frame">
          <div class="photo-fill building-exterior" role="img" aria-label="Photo of the apartment building and parking lot"></div>
        </div>
      </div>
      <p class="sign-phone">205-555-0148</p>
    </section>
  </main>
</body>
</html>
```